Email Template Design For Constant Contact Platform

I need an email ad template for sending out special offers to my customer email list. It has to work with Constant Contact. It needs to have an area for a product image, a description area, etc. The design should allow me to customize/change out the image and descriptions within the Constant Contacts platform. I have attached a bad example of an ad for my first email blast. There will need to be URL links to take the customer to our website.

Target Market(s)

B to B Lab Supplies and Equipment Buyers

Industry/Entity Type

Life Science and Industrial Laboratories

Font styles to use
Sans Serif

Requirements
Must have
• Project must work within Constant Contact and allow user changeable images and descriptions
Nice to have
• I'm looking for a template that allows me to insert new content and images for any new campaign

```html
<!DOCTYPE html>
<html lang="en">
<head>
<meta charset="utf-8">
<title>Meridian Lab Supply – Special Offer</title>
<link href="https://fonts.googleapis.com/css2?family=Poppins:wght@400;500;600;700;800&display=swap" rel="stylesheet">
<style>
  :root{
    --royal:#3a4cf0;
    --violet:#7a55ea;
    --sky:#5bc0f5;
    --hex-light:#9aa3f5;
    --hex-violet:#b3a2f4;
    --ink:#1b1b1b;
    --grey-text:#5a5a5a;
    --footer-grey:#e8e8e8;
    --ring:#7a55ea;
    --white:#ffffff;
  }
  *{box-sizing:border-box;margin:0;padding:0}
  html,body{width:1200px;height:4137px;overflow:hidden;background:var(--white)}
  body{position:relative;font-family:'Poppins',sans-serif;color:var(--ink)}
  .abs{position:absolute}

  /* header */
  .header{left:0;top:0;width:1200px;height:178px;background:var(--white)}
  .brand{left:0;width:1200px;top:30px;display:flex;justify-content:center;align-items:center;gap:18px}
  .brand-mark{width:62px;height:62px;border-radius:50%;background:var(--royal)}
  .brand-name{font-weight:700;font-size:40px;color:var(--ink);letter-spacing:1px}
  .header-contact{left:0;width:1200px;top:124px;text-align:center;font-weight:600;font-size:19px;color:var(--ink);word-spacing:4px}

  /* hero */
  .hero{left:0;top:178px;width:1200px;height:750px;background:linear-gradient(180deg,#9fb4cf 0%,#8fb7e2 45%,#6fc6f7 100%)}
  .hero-title{left:0;width:1200px;top:683px;text-align:center;color:var(--white);font-weight:700;font-size:61px;line-height:77px;text-transform:uppercase}

  /* feature bands */
  .band{left:0;width:1200px;overflow:hidden}
  .band-one{top:928px;height:374px;background:var(--royal)}
  .band-two{top:1302px;height:376px;background:var(--violet)}
  .band-copy{color:var(--white);font-size:26px;line-height:45px;font-weight:400}
  .band-one .band-copy{left:150px;top:117px;width:650px}
  .band-two .band-copy{left:419px;top:72px;width:640px}
  .hex{position:absolute}

  /* call to action */
  .cta{left:385px;top:1742px;width:429px;height:103px;background:var(--sky);color:var(--white);font-weight:700;font-size:32px;display:flex;align-items:center;justify-content:center;text-decoration:none;text-transform:uppercase}

  /* offer */
  .offer-band{left:0;top:2603px;width:1200px;height:643px;background:linear-gradient(180deg,#6b82f5 0%,#3a4cf0 45%,#0a16e0 100%)}
  .product-photo{left:180px;top:2200px;width:860px;height:560px;border-radius:24px;background:linear-gradient(135deg,#eceef2 0%,#c9ccd4 35%,#9ea2ac 55%,#d8dae0 75%,#f2f3f6 100%)}
  .offer-badge{left:369px;top:1970px;width:460px;height:460px}
  .offer-text{left:396px;width:406px;text-align:center;color:var(--white)}
  .offer-kicker{top:2070px;font-weight:700;font-size:34px;line-height:45px}
  .offer-value{top:2170px;font-weight:800;font-size:92px;line-height:110px}
  .offer-note{top:2290px;font-size:27px;line-height:36px}
  .offer-copy{left:130px;top:2820px;width:940px;text-align:center;color:var(--white);font-size:31px;line-height:45px}

  /* contact */
  .contact-icon{left:146px}
  .contact-label{left:222px;font-weight:600;font-size:34px;line-height:44px;color:var(--ink)}
  .contact-value{left:222px;font-size:26px;line-height:45px;color:var(--grey-text)}
  .notice{left:671px;top:3370px;width:382px;font-size:25px;line-height:45px;color:var(--grey-text);text-align:justify}

  /* footer */
  .legal-bar{left:0;top:3822px;width:1200px;height:105px;background:var(--footer-grey);display:flex;align-items:center;justify-content:center;font-size:27px;color:var(--grey-text)}
  .legal-bar a{color:var(--grey-text);text-decoration:none}
  .copyright{left:0;width:1200px;top:3956px;text-align:center;font-size:26px;color:var(--grey-text)}
  .site-bar{left:0;top:4033px;width:1200px;height:104px;background:var(--royal)}
  .site-url{left:0;width:1200px;top:36px;text-align:center;color:var(--white);font-size:27px;letter-spacing:9px}
  .site-code{right:55px;top:40px;color:var(--white);font-size:22px}
</style>
</head>
<body>

<header class="abs header">
  <div class="abs brand">
    <span class="brand-mark"></span>
    <span class="brand-name">MERIDIAN LAB SUPPLY</span>
  </div>
  <p class="abs header-contact">www.meridianlabco.com &nbsp;800-555-0142</p>
</header>

<section class="abs hero" role="img" aria-label="Photo of a scientist in safety glasses working with a pipette in a laboratory"></section>
<h1 class="abs hero-title">All your<br>laboratory supplies</h1>

<section class="abs band band-one">
  <p class="abs band-copy">At our store, we're proud to offer a wide range of Deep Core Samplers in all sizes and shapes. So why wait?</p>
  <svg class="hex" style="left:860px;top:0" width="340" height="374" viewBox="0 0 340 374" role="img" aria-label="Icon of a researcher at a microscope">
    <polygon points="170,2 340,95 340,280 170,372 0,280 0,95" fill="var(--hex-light)"/>
  </svg>
</section>

<section class="abs band band-two">
  <svg class="hex" style="left:0;top:0" width="340" height="376" viewBox="0 0 340 376" role="img" aria-label="Icon of laboratory glassware">
    <polygon points="169,2 339,95 339,282 169,374 -1,282 -1,95" fill="var(--hex-violet)"/>
  </svg>
  <p class="abs band-copy">Head over to our website now and browse our selection of Deep Core Samplers. With our unbeatable prices, you're sure to find the perfect one for your application.</p>
</section>

<a class="abs cta" href="#">Browse samplers</a>

<section class="abs offer-band"></section>
<div class="abs product-photo" role="img" aria-label="Product photo of a stainless steel sampler cylinder"></div>

<svg class="abs offer-badge" width="460" height="460" viewBox="0 0 460 460" aria-hidden="true">
  <circle cx="230" cy="230" r="228" fill="var(--white)" stroke="var(--ring)" stroke-width="4"/>
  <circle cx="230" cy="230" r="203" fill="var(--royal)"/>
</svg>
<p class="abs offer-text offer-kicker">Our Special<br>Offer</p>
<p class="abs offer-text offer-value">50%</p>
<p class="abs offer-text offer-note">For this product</p>

<p class="abs offer-copy">Lorem ipsum dolor sit amet, consectetur adip iscing elit, sed do eiusmod tempor incididunt ut labore et dolore magna aliqua. Ut enim ad minim veniam, quis nostrud exercitation ullamco laboris nisi ut aliquip ex ea commodo consequat. Duis aute irure dolor in repreh enderit in voluptate velit esse cillum dolore eu fugiat nulla pariatur.</p>

<svg class="abs contact-icon" style="top:3382px" width="32" height="44" viewBox="0 0 32 44" aria-hidden="true">
  <path d="M16 0C7 0 0 7 0 16c0 11 16 28 16 28s16-17 16-28C32 7 25 0 16 0z" fill="var(--violet)"/>
  <circle cx="16" cy="16" r="6" fill="var(--white)"/>
</svg>
<p class="abs contact-label" style="top:3370px">Address:</p>
<p class="abs contact-value" style="top:3417px">1420 Harbor Lane<br>Fairview, TX 77000 USA</p>

<svg class="abs contact-icon" style="top:3553px" width="48" height="34" viewBox="0 0 48 34" aria-hidden="true">
  <rect width="48" height="34" rx="3" fill="var(--violet)"/>
  <path d="M2 3l22 16L46 3" fill="none" stroke="var(--white)" stroke-width="3"/>
</svg>
<p class="abs contact-label" style="top:3546px">Email :</p>
<p class="abs contact-value" style="top:3592px">sales@meridianlabco.com</p>

<svg class="abs contact-icon" style="top:3668px;left:150px" width="40" height="40" viewBox="0 0 24 24" aria-hidden="true">
  <path d="M6.6 10.8c1.4 2.8 3.8 5.1 6.6 6.6l2.2-2.2c.3-.3.7-.4 1-.2 1.1.4 2.3.6 3.6.6.6 0 1 .4 1 1V20c0 .6-.4 1-1 1C10.6 21 3 13.4 3 4c0-.6.4-1 1-1h3.5c.6 0 1 .4 1 1 0 1.3.2 2.5.6 3.6.1.3 0 .7-.2 1l-2.3 2.2z" fill="var(--violet)"/>
</svg>
<p class="abs contact-label" style="top:3666px">Phone :</p>
<p class="abs contact-value" style="top:3713px">800-555-0142</p>

<p class="abs notice">You are receiving this email because you have visited our site or asked us about the regular newsletter.</p>

<nav class="abs legal-bar">
  <a href="#">Terms and Conditions</a>&nbsp;|&nbsp;<a href="#">Privacy Policy</a>&nbsp;|&nbsp;<a href="#">Unsubscribe</a>
</nav>
<p class="abs copyright">© 2024 Meridian Lab Supply | All rights reserved.</p>

<footer class="abs site-bar">
  <p class="abs site-url">WWW.MERIDIANLABCO.COM</p>
  <span class="abs site-code">C38</span>
</footer>

</body>
</html>
```